Kitchen Tools Infographic - Helpful Items for Healthy Home Meals

We are a weight loss company that provides holistic, natural nutrition programs to consumers -- you can see our web site at www.FernQuill.com. We need a simple infographic to be shared on social media and via email. The topic for the infographic is "Equip Your Kitchen for Healthy Home Meals". We've outlined 5 groups of kitchen tools that are helpful for consumers to have for preparing home meals, and included some framing statistics emphasizing the weight management benefits of preparing meals versus eating out.

Target Market(s)

Women age 35-55

Industry/Entity Type

Health And Wellness

Font styles to use
Sans Serif

Colors
0292cd
9bcb3b

Requirements
Must have
• - FernQuill Logo
• - Graphics summarizing statistic (weight gain)
• - Graphics showing groupings of kitchen tools
Should not have
• body scale graphics
• before/after graphics

```html
<!DOCTYPE html>
<html lang="en">
<head>
<meta charset="utf-8">
<title>Equip Your Kitchen for Healthy Home Meals</title>
<link rel="stylesheet" href="https://fonts.googleapis.com/css2?family=Open+Sans:ital,wght@0,400;0,600;0,700;1,700&family=Shadows+Into+Light+Two&display=swap">
<style>
:root{
  --blue:#0292cd;
  --green:#9bcb3b;
  --green-dark:#6f9a2a;
  --orange:#f7941d;
  --ink:#231f20;
  --text:#333333;
  --band:#eeeeef;
  --panel:#ececec;
  --footer:#231f20;
}
*{margin:0;padding:0;box-sizing:border-box}
html,body{width:1200px;height:2571px;overflow:hidden;background:#fff}
body{position:relative;font-family:"Open Sans",Arial,sans-serif;color:var(--text)}
.header-fold{position:absolute;left:0;top:100px;width:40px;height:40px;background:var(--green-dark);clip-path:polygon(0 0,100% 0,100% 100%)}
.header{position:absolute;left:0;top:0;width:1200px;height:128px;background:var(--green);
  clip-path:polygon(0 0,100% 0,100% 100%,0 100%)}
.title{position:absolute;left:50px;top:22px;font-family:"Shadows Into Light Two",cursive;font-size:62px;font-weight:400;color:var(--ink);line-height:1.2;white-space:nowrap}
.intro{position:absolute;left:40px;top:128px;width:1160px;height:185px;background:var(--panel);padding:20px 60px 0 70px}
.intro h2{color:var(--blue);font-size:32px;font-weight:700;text-align:center;margin-bottom:8px}
.intro p{font-size:24px;line-height:1.45;color:var(--ink)}
.intro em{font-weight:700}
.charts{position:absolute;left:0;top:310px}
.tools-banner{position:absolute;left:85px;top:770px;width:1015px;height:68px;background:var(--orange);
  clip-path:polygon(0 0,100% 0,96% 100%,4% 100%);color:var(--ink);font-size:36px;text-align:center;line-height:68px;white-space:nowrap}
.tools-banner b{font-weight:700}
.spine{position:absolute;left:1021px;top:835px;width:8px;height:1455px;background:var(--orange)}
.row{position:absolute;left:0;width:1025px;height:255px;background:var(--band)}
.item{position:absolute;top:36px;width:320px}
.icon{width:130px;height:110px;margin:0 auto 12px;border-radius:10px}
.item h3{font-size:20px;font-weight:700;text-align:center;color:var(--ink)}
.row.blue-titles h3{color:var(--blue)}
.item p{font-size:16px;line-height:1.35;color:var(--ink);padding:2px 20px 0;text-align:left}
.badge{position:absolute;right:0;width:300px;height:230px}
.badge text{font-family:"Open Sans",Arial,sans-serif;font-weight:700}
.footer{position:absolute;left:0;top:2290px;width:1200px;height:281px;background:var(--footer);border-top:8px solid var(--green)}
.footer .pitch{position:absolute;top:30px;width:100%;text-align:center;color:#fff;font-size:25px;font-weight:700}
.footer .invite{position:absolute;top:88px;width:100%;text-align:center;color:var(--green);font-size:24px;font-weight:700}
.contact{position:absolute;left:480px;top:138px;width:250px;height:44px;background:var(--green);color:var(--ink);font-weight:700;font-size:24px;text-align:center;line-height:44px}
.brand{position:absolute;left:28px;top:178px;color:var(--blue);font-size:62px;font-weight:600;letter-spacing:1px}
.site{position:absolute;right:32px;top:205px;color:#fff;font-size:24px;font-weight:700}
</style>
</head>
<body>

<header class="header"><h1 class="title">Equip Your Kitchen for Healthy HomeMeals</h1></header>
<div class="header-fold"></div>

<section class="intro">
  <h2>Why Cook at Home?</h2>
  <p>Those who eat out consume an average of 134 calories more per meal. <em>Americans eat out an average of 4.5 times per week</em>, so those extra calories can add up to substantial weight gain -- and give you a reason to prepare your own meals.</p>
</section>

<svg class="charts" width="1200" height="460" viewBox="0 0 1200 460" font-family="Open Sans, Arial, sans-serif">
  <g fill="#231f20" font-size="22" text-anchor="end">
    <text x="82" y="357">0</text><text x="82" y="310">100</text><text x="82" y="263">200</text><text x="82" y="216">300</text>
    <text x="82" y="169">400</text><text x="82" y="122">500</text><text x="82" y="75">600</text><text x="82" y="28">700</text>
  </g>
  <line x1="95" y1="10" x2="95" y2="350" stroke="#231f20" stroke-width="2"/>
  <line x1="95" y1="350" x2="460" y2="350" stroke="#231f20" stroke-width="2"/>
  <line x1="95" y1="67" x2="185" y2="67" stroke="#231f20" stroke-width="2" stroke-dasharray="10 6"/>
  <line x1="95" y1="282" x2="440" y2="282" stroke="#231f20" stroke-width="2" stroke-dasharray="10 6"/>
  <rect x="185" y="67" width="36" height="283" fill="var(--blue)"/>
  <rect x="385" y="282" width="36" height="68" fill="var(--green)"/>
  <text x="203" y="378" font-size="18" fill="var(--blue)" text-anchor="middle">Calories per week</text>
  <text x="403" y="378" font-size="18" fill="#231f20" text-anchor="middle">Calories per meal</text>
  <text x="30" y="430" font-size="24" fill="#231f20">Excess Calories from Restaurant Meals</text>
  <line x1="25" y1="445" x2="520" y2="445" stroke="#231f20" stroke-width="2"/>

  <g fill="#231f20" font-size="22" text-anchor="end">
    <text x="728" y="357">0</text><text x="728" y="311">2</text><text x="728" y="265">4</text>
    <text x="728" y="219">6</text><text x="728" y="173">8</text><text x="728" y="127">10</text>
  </g>
  <line x1="740" y1="10" x2="740" y2="350" stroke="#231f20" stroke-width="2"/>
  <line x1="740" y1="350" x2="1110" y2="350" stroke="#231f20" stroke-width="2"/>
  <line x1="740" y1="332" x2="770" y2="332" stroke="#231f20" stroke-width="2" stroke-dasharray="10 6"/>
  <line x1="740" y1="246" x2="910" y2="246" stroke="#231f20" stroke-width="2" stroke-dasharray="10 6"/>
  <line x1="740" y1="142" x2="1055" y2="142" stroke="#231f20" stroke-width="2" stroke-dasharray="10 6"/>
  <rect x="770" y="332" width="32" height="18" fill="var(--blue)"/>
  <rect x="910" y="246" width="34" height="104" fill="var(--green)"/>
  <rect x="1055" y="142" width="34" height="208" fill="var(--blue)"/>
  <text x="786" y="378" font-size="18" fill="var(--blue)" text-anchor="middle">2 months</text>
  <text x="927" y="378" font-size="18" fill="#231f20" text-anchor="middle">6 months</text>
  <text x="1072" y="378" font-size="18" fill="var(--blue)" text-anchor="middle">1 year</text>
  <text x="685" y="430" font-size="24" fill="#231f20">Pounds Gained from Restaurant Meals</text>
  <line x1="680" y1="445" x2="1175" y2="445" stroke="#231f20" stroke-width="2"/>
</svg>

<div class="tools-banner">Make healthy eating easier with these <b>Kitchen Tools</b>:</div>
<div class="spine"></div>

<section class="row blue-titles" style="top:866px">
  <div class="item" style="left:5px"><div class="icon" role="img" aria-label="Wooden cutting board" style="background:#d08a4e"></div><h3>Cutting Board</h3><p>essential for prepping meat and vegetables</p></div>
  <div class="item" style="left:295px"><div class="icon" role="img" aria-label="Chef's knife" style="background:#c9ccd0;height:40px;margin-top:35px;margin-bottom:47px"></div><h3>Chef’s Knife</h3><p>go for quality to make chopping, dicing and slicing faster and easier</p></div>
  <div class="item" style="left:595px"><div class="icon" role="img" aria-label="Digital food scale" style="background:#f6b428"></div><h3>Digital Food Scale</h3><p>get the precision you need for perfect recipes and portion control</p></div>
</section>
<svg class="badge" style="top:886px" viewBox="0 0 300 230" role="img" aria-label="Step 1 Prep">
  <polygon points="150,8 292,115 150,222 8,115" fill="#fff" stroke="var(--blue)" stroke-width="14"/>
  <text x="150" y="100" font-size="52" fill="var(--blue)" text-anchor="middle">1</text>
  <text x="150" y="150" font-size="40" fill="var(--blue)" text-anchor="middle">PREP</text>
</svg>

<section class="row" style="top:1140px">
  <div class="item" style="left:5px"><div class="icon" role="img" aria-label="High-powered blender" style="background:#7cb342"></div><h3>High-Powered Blender</h3><p>make highly nutritious, healthy drinks from fruits and veggies</p></div>
  <div class="item" style="left:295px"><div class="icon" role="img" aria-label="Slow cooker" style="background:#37474f"></div><h3>Slow Cooker</h3><p>cook delicious meals while you are at work</p></div>
  <div class="item" style="left:595px"><div class="icon" role="img" aria-label="Pressure cooker" style="background:#f9c316"></div><h3>Pressure Cooker</h3><p>create single pot meals in 20 minutes or less</p></div>
</section>
<svg class="badge" style="top:1160px" viewBox="0 0 300 230" role="img" aria-label="Step 2 Tech">
  <polygon points="150,8 292,115 150,222 8,115" fill="#fff" stroke="var(--green)" stroke-width="14"/>
  <text x="150" y="100" font-size="52" fill="var(--green)" text-anchor="middle">2</text>
  <text x="150" y="150" font-size="40" fill="var(--green)" text-anchor="middle">TECH</text>
</svg>

<section class="row blue-titles" style="top:1414px">
  <div class="item" style="left:5px"><div class="icon" role="img" aria-label="Ceramic frying pan" style="background:#263238;border-radius:50%;width:110px"></div><h3>Ceramic Pan</h3><p>nonstick cooking surface allows you to cook without oil</p></div>
  <div class="item" style="left:295px"><div class="icon" role="img" aria-label="Vegetable steamer" style="background:#e95b3c"></div><h3>Vegetable Steamer</h3><p>preserve nutrients and natural, fresh taste</p></div>
  <div class="item" style="left:595px"><div class="icon" role="img" aria-label="Baking sheet" style="background:#5a1f23"></div><h3>Baking Sheet</h3><p>ideal for roasting vegetables in the oven or baking chicken and fish dishes</p></div>
</section>
<svg class="badge" style="top:1434px" viewBox="0 0 300 230" role="img" aria-label="Step 3 Cook">
  <polygon points="150,8 292,115 150,222 8,115" fill="#fff" stroke="var(--blue)" stroke-width="14"/>
  <text x="150" y="100" font-size="52" fill="var(--blue)" text-anchor="middle">3</text>
  <text x="150" y="150" font-size="40" fill="var(--blue)" text-anchor="middle">COOK</text>
</svg>

<section class="row" style="top:1689px">
  <div class="item" style="left:5px"><div class="icon" role="img" aria-label="Red checked cloth napkin" style="background:#e2262f"></div><h3>Cloth Napkins</h3><p>to reduce waste and dress up your table</p></div>
  <div class="item" style="left:295px"><div class="icon" role="img" aria-label="Dinner plate with fork and spoon" style="background:#dfe1e3"></div><h3>Dinnerware</h3><p>pre-plate meals rather than serving family style to control portions</p></div>
  <div class="item" style="left:595px"><div class="icon" role="img" aria-label="Small plates" style="background:#e6e8ea"></div><h3>Small Plates</h3><p>use salad plates and smaller dishware to manage perception of food volume</p></div>
</section>
<svg class="badge" style="top:1709px" viewBox="0 0 300 230" role="img" aria-label="Step 4 Serve">
  <polygon points="150,8 292,115 150,222 8,115" fill="#fff" stroke="var(--green)" stroke-width="14"/>
  <text x="150" y="100" font-size="52" fill="var(--green)" text-anchor="middle">4</text>
  <text x="150" y="150" font-size="40" fill="var(--green)" text-anchor="middle">SERVE</text>
</svg>

<section class="row blue-titles" style="top:1964px">
  <div class="item" style="left:5px"><div class="icon" role="img" aria-label="Glass storage containers" style="background:#cfe8f3"></div><h3>Glass Storage Containers</h3><p>keep your healthy leftovers so nothing goes to waste</p></div>
  <div class="item" style="left:295px"><div class="icon" role="img" aria-label="Mason jar" style="background:#f3b6c8;width:80px"></div><h3>Mason Jars</h3><p>perfect for premade salads that you can bring to work</p></div>
  <div class="item" style="left:595px"><div class="icon" role="img" aria-label="Re-sealable freezer bag" style="background:#e9ecef"></div><h3>Freezer Safe Re-Sealable Bags</h3><p>prepare double batches to make the most of your time</p></div>
</section>
<svg class="badge" style="top:1984px" viewBox="0 0 300 230" role="img" aria-label="Step 5 Store">
  <polygon points="150,8 292,115 150,222 8,115" fill="#fff" stroke="var(--blue)" stroke-width="14"/>
  <text x="150" y="100" font-size="52" fill="var(--blue)" text-anchor="middle">5</text>
  <text x="150" y="150" font-size="40" fill="var(--blue)" text-anchor="middle">STORE</text>
</svg>

<footer class="footer">
  <p class="pitch">FernQuill can help you develop healthier eating habits.</p>
  <p class="invite">We invite you to learn more.</p>
  <div class="contact">CONTACT US</div>
  <div class="brand">FernQuill</div>
  <div class="site">www.FernQuill.com</div>
</footer>

</body>
</html>
```